Calendar Ad / Flyer

Our law firm needs a calendar ad to place in a local calendar.
THE DEADLINE IS THIS THURSDAY 06/28/2018.

Attached is the ad used in last years calendar. A few notes on this...
**. This is by no means the model to follow.
Please be creative and do what makes more sense marketing wise.
1. Need to update the color scheme which corresponds to the new website at morvanlegal.net
2. The "MORVAN LEGAL | STANDING FIRM FOR YOUR FUTURE" should be put at the top and made larger
3. "KNOWN AND TRUSTED IN OUR COMMUNITY FOR OVER 21 YEARS" should be changed to "KNOWN AND TRUSTED IN OUR COMMUNITY FOR OVER 22 YEARS"
4. "Dorian K. Morvan, Esq." should be made larger and better positioned.
5. Under the list of practices, it should be changed to have:
"Personal Injury, Legal Malpractice, Unlicensed Contractors, Medical Malpractice, Civil Litigation"
6. Contact information (i.e. contact number, website, and address) should be better positioned
7. Placement of endorsement logos should stand out more.
8. New picture of head attorney is attached.

Last but not least... Give it your best shot!

```html
<!DOCTYPE html>
<html lang="en">
<head>
<meta charset="UTF-8">
<title>Morvan Legal – Calendar Ad</title>
<link rel="stylesheet" href="https://fonts.googleapis.com/css2?family=Lato:wght@400;700;900&display=swap">
<style>
  :root {
    --gold: #c9a46f;
    --gold-light: #d6b888;
    --slate: #76777b;
    --slate-dark: #444447;
    --charcoal: #333234;
    --ink: #5a5a5c;
    --white: #ffffff;
    --paper: #f1f1f1;
    --tagline: #dcdcdc;
    --badge-red: #8e2a2c;
    --badge-crimson: #c4262e;
    --badge-tan: #b39a68;
    --badge-blue: #2a63a6;
    --badge-sky: #3a95d4;
  }
  * { margin: 0; padding: 0; box-sizing: border-box; }
  html, body { width: 1200px; height: 900px; overflow: hidden; background: var(--white); }
  .ad {
    position: relative;
    width: 1200px;
    height: 900px;
    overflow: hidden;
    font-family: "Lato", Arial, sans-serif;
  }
  .ad-shapes { position: absolute; inset: 0; }
  .brand {
    position: absolute;
    left: 94px;
    top: 134px;
    display: flex;
    align-items: center;
    gap: 18px;
  }
  .brand-mark { width: 34px; height: 34px; background: var(--gold); }
  .brand-name {
    font-size: 56px;
    font-weight: 700;
    letter-spacing: 6px;
    color: var(--gold);
    line-height: 1;
  }
  .brand-tagline {
    position: absolute;
    left: 228px;
    top: 193px;
    font-size: 20px;
    font-weight: 700;
    letter-spacing: 1px;
    color: var(--tagline);
  }
  .attorney-name {
    position: absolute;
    left: 84px;
    top: 320px;
    font-size: 45px;
    font-weight: 900;
    color: var(--white);
    line-height: 1;
  }
  .attorney-tenure {
    position: absolute;
    left: 86px;
    top: 376px;
    font-size: 22px;
    line-height: 30px;
    color: var(--white);
  }
  .practice-list {
    position: absolute;
    left: 94px;
    top: 530px;
    list-style: none;
  }
  .practice-list li {
    display: flex;
    align-items: center;
    height: 46.5px;
    font-size: 29px;
    color: var(--white);
    letter-spacing: 0.5px;
  }
  .practice-list li svg { width: 16px; height: 18px; margin-right: 22px; }
  .contact-phone, .contact-web {
    position: absolute;
    top: 812px;
    display: flex;
    align-items: center;
    font-size: 38px;
    font-weight: 700;
    color: var(--ink);
    line-height: 1;
  }
  .contact-phone { left: 84px; }
  .contact-web { left: 438px; font-weight: 400; }
  .contact-phone svg, .contact-web svg { margin-right: 10px; }
  .contact-address {
    position: absolute;
    left: 888px;
    top: 798px;
    font-size: 18.5px;
    font-style: normal;
    font-weight: 700;
    line-height: 29px;
    color: var(--white);
  }
</style>
</head>
<body>
<div class="ad">
  <svg class="ad-shapes" width="1200" height="900" viewBox="0 0 1200 900">
    <defs>
      <linearGradient id="header-fade" x1="0" y1="0" x2="1" y2="0">
        <stop offset="0" stop-color="#5f5f62"/>
        <stop offset="1" stop-color="#7d7e82"/>
      </linearGradient>
      <linearGradient id="paper-fade" x1="0" y1="0" x2="1" y2="1">
        <stop offset="0" stop-color="#ffffff"/>
        <stop offset="1" stop-color="#e9e9ea"/>
      </linearGradient>
      <linearGradient id="portrait-tone" x1="0" y1="0" x2="0" y2="1">
        <stop offset="0" stop-color="#7f746c"/>
        <stop offset="0.55" stop-color="#a88f7e"/>
        <stop offset="0.8" stop-color="#707174"/>
        <stop offset="1" stop-color="#5e5f63"/>
      </linearGradient>
    </defs>
    <rect x="0" y="0" width="1200" height="252" fill="url(#header-fade)"/>
    <polygon points="0,0 250,0 365,252 0,252" fill="var(--slate-dark)"/>
    <rect x="0" y="252" width="1200" height="250" fill="var(--gold)"/>
    <rect x="0" y="502" width="1200" height="278" fill="url(#paper-fade)"/>
    <polygon points="0,502 576,502 806,780 0,780" fill="var(--charcoal)"/>
    <rect x="0" y="780" width="1200" height="120" fill="var(--white)"/>
    <polygon points="821,787 1200,787 1200,870 893,870" fill="var(--gold)"/>
    <polygon points="0,878 900,878 918,900 0,900" fill="var(--gold-light)"/>
    <path role="img" aria-label="Portrait photograph of the head attorney in a grey suit, white shirt and blue tie"
          d="M520,502 C528,452 548,440 610,428 L860,380 L860,40 C860,16 876,0 900,0 L1200,0 L1200,502 Z"
          fill="url(#portrait-tone)"/>
    <g class="endorsements">
      <circle role="img" aria-label="Million dollar advocates membership badge" cx="800" cy="600" r="42" fill="var(--badge-red)"/>
      <rect role="img" aria-label="Five-star review listing badge" x="900" y="568" width="92" height="64" rx="2" fill="var(--badge-crimson)"/>
      <rect role="img" aria-label="Peer-rated lawyer listing badge" x="1052" y="568" width="88" height="64" rx="8" fill="var(--badge-tan)"/>
      <rect role="img" aria-label="Accredited business A+ rating badge" x="847" y="680" width="123" height="46" rx="4" fill="var(--badge-blue)"/>
      <circle role="img" aria-label="Top attorney 10.0 rating badge" cx="1061" cy="701" r="38" fill="var(--badge-sky)"/>
    </g>
  </svg>

  <div class="brand">
    <span class="brand-name">MORVAN LEGAL</span>
    <span class="brand-mark"></span>
  </div>
  <div class="brand-tagline">STANDING FIRM FOR YOUR FUTURE</div>

  <h1 class="attorney-name">DORIAN K. MORVAN, ESQ.</h1>
  <p class="attorney-tenure">KNOWN AND TRUSTED IN OUR COMMUNITY<br>FOR OVER 22 YEARS</p>

  <ul class="practice-list">
    <li><svg viewBox="0 0 16 18"><polygon points="0,0 16,9 0,18 5,9" fill="#c9a46f"/></svg>PERSONAL INJURY</li>
    <li><svg viewBox="0 0 16 18"><polygon points="0,0 16,9 0,18 5,9" fill="#c9a46f"/></svg>LEGAL MALPRACTICE</li>
    <li><svg viewBox="0 0 16 18"><polygon points="0,0 16,9 0,18 5,9" fill="#c9a46f"/></svg>UNLICENSED CONTRACTORS</li>
    <li><svg viewBox="0 0 16 18"><polygon points="0,0 16,9 0,18 5,9" fill="#c9a46f"/></svg>MEDICAL MALPRACTICE</li>
    <li><svg viewBox="0 0 16 18"><polygon points="0,0 16,9 0,18 5,9" fill="#c9a46f"/></svg>CIVIL LITIGATION</li>
  </ul>

  <div class="contact-phone">
    <svg width="24" height="40" viewBox="0 0 24 40"><path d="M6,2 L11,2 L12,11 L8,13 Q8,20 12,28 L16,27 L20,35 L15,38 Q2,34 2,12 Q2,4 6,2 Z" fill="#c9a46f"/></svg>
    (888) 555-0147
  </div>
  <div class="contact-web">
    <svg width="34" height="34" viewBox="0 0 34 34" fill="none" stroke="#c9a46f" stroke-width="2"><circle cx="17" cy="17" r="15"/><ellipse cx="17" cy="17" rx="7" ry="15"/><line x1="2" y1="17" x2="32" y2="17"/><line x1="17" y1="2" x2="17" y2="32"/><path d="M5,9 H29 M5,25 H29"/></svg>
    morvanlegal.net
  </div>
  <address class="contact-address">4120 Larkspur Ave. | Suite 305<br>Westfield, CA | 90418</address>
</div>
</body>
</html>
```